Hi, Kelvar Woodworks is a Tasmanian based business specialising in fine woodcraft and laser engraving. We produce high quality products using beautiful Tasmanian timbers.We have a logo that we aren't entirely happy with. We don't feel that it stands out or really speaks about who we are as a business. We would like for the new logo to contain the map of Tasmania and perhaps use modern earthy colours in the design to make it pop. The final design should communicate the natural beauty of Tasmanian timbers and the creativity of the artwork. Thank you.

Target Market(s)

They range from souvenir items through to gallery artworks( photos included show some of the different timbers used in the inlay and intarsia pieces.

Industry/Entity Type

Business

Contact Information for Business Card

www.kelvarwoodworks.example
email: kelvarwoodworks@mailhaven.example
Gus Merriwether of 0452 806 194

Requirements
Must have
• Our logo must have the Map of Tasmania and the words Kelvar Woodworks. ( see photo of current logo below) We are open to your ideas of how that could be incorporated into the design.The reverse side of the card would have our email/wesite addresses.. Our website if you need further ideas is www.kelvarwoodworks.example and include a phone number for Gus Merriwether of 0452 806 194
Nice to have
• The font style could reflect elegance and beauty and can be decided by the designer

```html
<!DOCTYPE html>
<html lang="en">
<head>
<meta charset="utf-8">
<title>Kelvar Woodworks – Business Card</title>
<link rel="stylesheet" href="https://fonts.googleapis.com/css2?family=Libre+Baskerville:wght@700&family=Open+Sans:wght@400&display=swap">
<style>
  :root {
    --page: #ffffff;
    --card-edge: #d9cfc4;
    --beige: #e9d7c3;
    --grain-light: #f6ede3;
    --grain-tone: #e7d3bd;
    --wood-mid: #8a5a34;
    --wood-dark: #5a3820;
    --cream: #f3e4cf;
    --ink: #2a1a10;
  }
  * { box-sizing: border-box; margin: 0; padding: 0; }
  html, body {
    width: 847px; height: 1200px; overflow: hidden;
    background: var(--page);
  }
  .canvas { position: relative; width: 847px; height: 1200px; }

  .card {
    position: absolute; left: 28px; width: 793px; height: 468px;
    border: 1px solid var(--card-edge); overflow: hidden;
  }
  .card--front { top: 126px; background: var(--beige); }
  .card--back { top: 630px; }

  .grain-strip {
    position: absolute; left: 0; top: 0; width: 98px; height: 100%;
    background: linear-gradient(90deg, var(--grain-light), var(--grain-tone) 50%, var(--grain-light));
  }
  .grain-field {
    position: absolute; inset: 0;
    background: linear-gradient(100deg, var(--grain-light), var(--grain-tone) 45%, var(--grain-light) 70%, var(--grain-tone));
  }

  .logo-disc {
    position: absolute; border-radius: 50%;
    background: radial-gradient(circle at 50% 45%, var(--wood-mid), var(--wood-dark));
    display: flex; align-items: center; justify-content: center; text-align: center;
  }
  .card--front .logo-disc { left: 48px; top: 74px; width: 320px; height: 320px; }
  .card--back .logo-disc { left: 208px; top: 46px; width: 376px; height: 376px; }

  .logo-name {
    font-family: "Libre Baskerville", serif; font-weight: 700;
    color: var(--cream); text-transform: uppercase; line-height: 1.25;
  }
  .card--front .logo-name { font-size: 30px; }
  .card--back .logo-name { font-size: 36px; }

  .holder {
    position: absolute; left: 430px; top: 152px;
    font-family: "Libre Baskerville", serif; font-weight: 700;
    font-size: 25px; color: var(--ink); text-transform: uppercase; letter-spacing: 0.3px;
    white-space: nowrap;
  }
  .contact {
    position: absolute; left: 432px; top: 218px; list-style: none;
    font-family: "Open Sans", sans-serif; font-size: 15px; color: var(--ink);
  }
  .contact li { display: flex; align-items: center; height: 36px; white-space: nowrap; }
  .contact svg { width: 28px; height: 20px; margin-right: 14px; flex: none; }
  .website {
    position: absolute; left: 440px; top: 410px;
    font-family: "Open Sans", sans-serif; font-size: 15px; color: var(--ink);
    white-space: nowrap;
  }
</style>
</head>
<body>
<main class="canvas">
  <section class="card card--front">
    <div class="grain-strip" role="img" aria-label="Light wood grain pattern"></div>
    <div class="logo-disc">
      <span class="logo-name">Kelvar<br>Woodworks</span>
    </div>
    <h1 class="holder">Gus Merriwether</h1>
    <ul class="contact">
      <li>
        <svg viewBox="0 0 30 22" aria-hidden="true">
          <path d="M3 7 Q15 0 27 7 L25 10 L20 8 L19 5 Q15 4 11 5 L10 8 L5 10 Z" fill="var(--ink)"/>
          <rect x="7" y="11" width="16" height="10" rx="2" fill="var(--ink)"/>
          <circle cx="15" cy="16" r="3" fill="var(--beige)"/>
        </svg>
        0452 806 194
      </li>
      <li>
        <svg viewBox="0 0 30 22" aria-hidden="true">
          <rect x="2" y="2" width="26" height="18" fill="var(--ink)"/>
          <path d="M3 3 L15 13 L27 3" fill="none" stroke="var(--beige)" stroke-width="2"/>
        </svg>
        kelvarwoodworks@mailhaven.example
      </li>
    </ul>
    <p class="website">www.kelvarwoodworks.example</p>
  </section>

  <section class="card card--back">
    <div class="grain-field" role="img" aria-label="Light wood grain pattern"></div>
    <div class="logo-disc">
      <span class="logo-name">Kelvar<br>Woodworks</span>
    </div>
  </section>
</main>
</body>
</html>
```